Wine Label for a Prosecco Wine Called Vuro

Prosecco is a white sparkling wine from Italy. We are looking for an eye catching, elegant label for this prosecco that is called "Vuro" because it is a young, fresh, lively white sparkling wine. (We do not want to see children or babies featured on the label-- just the name VURO please.) Attached is the old label for your reference, and the bottle type that will be used , which is a dark green Burgundy style bottle (pls ignore the label on the bottle). Please no grapes or wine glasses on the label. We are looking for something: eye catching / fun / ELEGANT (not cheap). We would be happy with a fun color too. Remember-- elegant, eye catching! Thanks!
Updates

Hi All, I think I made a mistake in my brief and have updated it. I also uploaded a competitor's label that we like very much to give better direction to what we are looking for. Also, the word Vuro cannot be vertical, nor can it be broken. It needs to read: VURO or Vuro. Thanks

Target Market(s)

American adults male and female.

Colors
abd036
33a6d7
33b8a4
ffcf3e

Requirements
Must have
• The mandatory information as shown on old labels. The word VURO should be very prominent.
Nice to have
• The uploaded photo of a competitor's prosecco shows a label we really like... if you could play around with this shape and style we'd be very happy.
Should not have
• No grape images, no wine glass images, no images of babies or children.

```html
<!DOCTYPE html>
<html lang="en">
<head>
<meta charset="utf-8">
<title>Vuro Prosecco – Label</title>
<link rel="stylesheet" href="https://fonts.googleapis.com/css2?family=EB+Garamond:wght@400;600&family=Montserrat:wght@700&display=swap">
<style>
  :root {
    --label-paper: #e7e7e8;
    --ink: #231f20;
  }
  * { margin: 0; padding: 0; box-sizing: border-box; }
  html, body {
    width: 1200px;
    height: 1200px;
    overflow: hidden;
    background: var(--label-paper);
  }
  .label {
    position: relative;
    width: 1200px;
    height: 1200px;
    background: var(--label-paper);
    color: var(--ink);
  }
  .label > * {
    position: absolute;
    left: 0;
    width: 100%;
    text-align: center;
    line-height: 1;
  }
  .brand-name {
    top: 262px;
    font-family: "EB Garamond", serif;
    font-weight: 600;
    font-size: 232px;
    letter-spacing: 2px;
  }
  .divider {
    top: 504px;
    left: 378px;
    width: 444px;
    height: 3px;
    background: var(--ink);
  }
  .wine-type {
    top: 566px;
    font-family: "Montserrat", sans-serif;
    font-weight: 700;
    font-size: 100px;
    letter-spacing: 1px;
  }
  .region {
    top: 758px;
    font-family: "EB Garamond", serif;
    font-weight: 400;
    font-size: 40px;
  }
  .designation {
    top: 810px;
    font-family: "EB Garamond", serif;
    font-weight: 400;
    font-size: 25px;
    letter-spacing: 1px;
  }
  .style {
    top: 894px;
    font-family: "EB Garamond", serif;
    font-weight: 400;
    font-size: 44px;
    letter-spacing: 1px;
  }
</style>
</head>
<body>
  <main class="label">
    <h1 class="brand-name">VURO</h1>
    <div class="divider"></div>
    <h2 class="wine-type">PROSECCO</h2>
    <p class="region">Veneto</p>
    <p class="designation">Indicazione Geografica Tipica</p>
    <p class="style">FRIZZANTE</p>
  </main>
</body>
</html>
```